Catchy Cards for Hospital

I run a rural hospital in Texas called Pelham Ridge Hospital and am in need of contemporary business cards for all of my Department Heads. While our logo is somewhat simplistic, I don't have the option of changing it at this time, so anything to make the rest of the card present the appearance of a modern, professional healthcare facility would be great. Although the attached files are in black, our hospital colors are in a copper brown and black. I need to be able to change the name and title on the card so I can get cards printed for various department heads.

Target Market(s)

Referring physicians, large hospital systems, national organizations, state and federal government

Industry/Entity Type

Hospital

Contact Information for Business Card

Name Derek Solano
Title CEO

Phone: Main 555-740-2386 & Direct xxxxxx
Fax xxxxx
derek.solano@pelhamrh.com
382 Wilmot Street Box 415
Brannock, Calder 76291

Font styles to use
Serif

Colors
f48340

Requirements
Must have
• Clean crisp lines and ability to modify names, titles and emails
• On the back "PelhamRidgeHospital.Com
Nice to have
• Needs to be in line with logo, which is a bit dated and not too appealing, but I'm hoping that the rest of the card can make up for that fact just a little bit.
• Hospital's colors are a copper brown, black and white
Should not have
• Shapes or anything distracting

```html
<!DOCTYPE html>
<html lang="en">
<head>
<meta charset="utf-8">
<title>Pelham Ridge Hospital – Business Card</title>
<link href="https://fonts.googleapis.com/css2?family=Roboto:wght@400;700&family=Roboto+Condensed:wght@700&display=swap" rel="stylesheet">
<style>
  :root {
    --backdrop: #5a4939;
    --ink: #000000;
    --paper: #f0f0f0;
    --white: #ffffff;
    --text-light: #f4f4f4;
  }
  * { box-sizing: border-box; margin: 0; padding: 0; }
  html, body {
    width: 1200px; height: 960px; overflow: hidden;
    background: var(--backdrop);
    font-family: "Roboto", Arial, sans-serif;
  }
  .card {
    position: absolute;
    width: 600px; height: 343px;
    overflow: hidden;
    background: var(--ink);
  }
  .card--front { left: 314px; top: 113px; }
  .card--back  { left: 311px; top: 472px; }

  .front-wave { position: absolute; inset: 0; width: 600px; height: 343px; }

  .contact {
    position: absolute; left: 30px; top: 26px;
    color: var(--text-light);
  }
  .contact__name {
    font-family: "Roboto Condensed", "Arial Narrow", sans-serif;
    font-weight: 700; font-size: 21px;
    line-height: 24px;
  }
  .contact__title { font-size: 14px; line-height: 20px; margin-top: 1px; }
  .contact__address { font-size: 14px; line-height: 18px; margin-top: 9px; }
  .contact__list { list-style: none; margin-top: 10px; font-size: 14px; }
  .contact__list li { display: flex; align-items: center; height: 19px; }
  .contact__icon { width: 13px; height: 13px; margin-right: 10px; flex: none; }

  .brand-name {
    position: absolute;
    font-family: "Roboto", Arial, sans-serif;
    font-weight: 700;
    line-height: 1.08;
  }
  .brand-name--front {
    left: 350px; top: 196px;
    font-size: 32px; color: var(--ink);
  }
  .brand-name--back {
    left: 0; right: 0; top: 100px;
    font-size: 38px; color: var(--white); text-align: center;
  }
  .back-url {
    position: absolute; left: 0; right: 0; top: 290px;
    text-align: center; color: var(--white);
    font-weight: 700; font-size: 14px;
  }
</style>
</head>
<body>

<section class="card card--front" aria-label="Business card front">
  <svg class="front-wave" viewBox="0 0 600 343" aria-hidden="true">
    <path d="M0 222 C60 252 120 274 180 272 C250 268 300 200 360 140 C420 85 480 58 600 56 L600 343 L0 343 Z" fill="var(--paper)"/>
    <path d="M0 222 C60 252 120 274 180 272 C250 268 300 200 360 140 C420 85 480 58 600 56" fill="none" stroke="var(--white)" stroke-width="8"/>
    <path d="M0 234 C62 264 122 286 184 284 C254 280 304 212 364 150 C424 96 484 68 600 66" fill="none" stroke="var(--ink)" stroke-width="3"/>
  </svg>

  <div class="contact">
    <h1 class="contact__name">DEREK SOLANO</h1>
    <p class="contact__title">CEO</p>
    <p class="contact__address">382 Wilmot Street Box 415<br>Brannock, Calder 76291</p>
    <ul class="contact__list">
      <li>
        <svg class="contact__icon" viewBox="0 0 16 16" aria-hidden="true"><path fill="currentColor" d="M3.5 1 L6 1 L7 5 L5 6.5 C6 8.8 7.3 10 9.5 11 L11 9 L15 10 L15 12.5 C15 14 14 15 12.5 15 C6.5 14.5 1.5 9.5 1 3.5 C1 2 2 1 3.5 1 Z"/></svg>
        555-740-2386
      </li>
      <li>
        <svg class="contact__icon" viewBox="0 0 16 16" aria-hidden="true"><path fill="currentColor" d="M4 1 H12 V5 H4 Z M1 6 H15 V12 H12 V10 H4 V12 H1 Z M4 11 H12 V15 H4 Z"/></svg>
        555-740-2419
      </li>
      <li>
        <svg class="contact__icon" viewBox="0 0 16 16" aria-hidden="true"><path fill="currentColor" d="M1 3 H15 V13 H1 Z"/><path fill="none" stroke="var(--ink)" stroke-width="1.4" d="M1.5 3.5 L8 9 L14.5 3.5"/></svg>
        derek.solano@pelhamrh.com
      </li>
      <li>
        <svg class="contact__icon" viewBox="0 0 16 16" aria-hidden="true"><circle cx="8" cy="8" r="7" fill="currentColor"/><path fill="none" stroke="var(--ink)" stroke-width="1.2" d="M1 8 H15 M8 1 C5 4 5 12 8 15 M8 1 C11 4 11 12 8 15"/></svg>
        PelhamRidgeHospital.Com
      </li>
    </ul>
  </div>

  <p class="brand-name brand-name--front">Pelham<br>Ridge<br>Hospital</p>
</section>

<section class="card card--back" aria-label="Business card back">
  <p class="brand-name brand-name--back">Pelham<br>Ridge<br>Hospital</p>
  <p class="back-url">www.PelhamRidgeHospital.Com</p>
</section>

</body>
</html>
```